Kestrel Nine (IT/Network Services)

Kestrel Nine, LLC provides technology services to small and medium businesses. Essentially, anytime you've every thought your business might need an "IT guy" to handle something you could instead call us to handle it. Basically, you can outsource your IT needs to us.

This is a brand new company and so we'll need a brand new website. I'd like to use WordPress to handle the site since that will make things easier for me to maintain in the long run.

The site should include a, more-or-less, static front page with the dynamic data occurring on pages linked from a navigational area.

I have a logo already designed that I would like to see used in the design. The one with "white" in the title is the official logo, just added some other versions for your perusal.

Color queues from the logo but feel free to add other colors where applicable.

The site should feel somewhat corporate but with a "younger" slant (something a 25-35 year old would enjoy).

Pages (either to be added initially or by me after design completion):
"About" section - includes company history, business philosophy, etc.
"Services" section - service options, service approach, service specifics
"Testimonials" section - (eventually)
"News" section - (eventually) industry news, company news, events, blog
Contact Links

Websites to view:
The two largest local competitors:
http://www.brimfieldsystemsco.com/
http://www.qmworkset.com/
Other local competitors:
http://www.pvrllc.com/
http://www.lorvanassociates.com/

Other info you might find useful:
Domain: knllc.com
Address:
517 Hollis Row E
Suite 812B
Nashville, TN 37219
Phone: 615-382-7140
Emails available for use/display:
info@knllc.com
sales@knllc.com

Target Market(s)

Our target clients are mainly small businesses (25 or less computer users) which means we're looking at a lot of start-ups or younger companies. We'll be interacting with many entrepreneurs and young business owners.

Requirements
Must have
• Need full WP theme (not a mockup)

```html
<!DOCTYPE html>
<html lang="en">
<head>
<meta charset="utf-8">
<title>Kestrel Nine, LLC</title>
<link rel="stylesheet" href="https://fonts.googleapis.com/css2?family=Audiowide&family=Jura:wght@400;500;600&family=Lato:ital,wght@0,400;0,700;1,700&display=swap">
<style>
:root{
  --orange:#f28a1e;
  --orange-dark:#e06d12;
  --ink:#3a3a3a;
  --grey:#6a6a6a;
  --light:#f3f3f3;
  --line:#d9d9d9;
  --panel:#e5e5e5;
  --dark-btn:#4a4a4a;
}
*{box-sizing:border-box;margin:0;padding:0}
html,body{width:1084px;height:1200px;overflow:hidden;background:#efefef}
body{font-family:'Lato',sans-serif;color:var(--ink)}
.canvas{position:relative;width:1084px;height:1200px;overflow:hidden;background:linear-gradient(#f6f6f6 0,#fafafa 480px,#f2f2f2 481px,#f4f4f4 950px,#ececec 951px)}
.abs{position:absolute}
.topbar{left:0;top:0;width:1084px;height:6px;background:#555}
.brand{left:95px;top:40px;width:270px;display:flex;align-items:center;gap:8px;white-space:nowrap;font-family:'Audiowide',sans-serif;font-size:24px;line-height:30px;color:#4a4a4a}
.brand .dot{flex:none;width:20px;height:20px;border-radius:50%;background:var(--orange)}
.nav{left:402px;top:50px;display:flex;gap:38px;white-space:nowrap;font-family:'Jura',sans-serif;font-weight:600;font-size:15px;color:#555}
.nav .current{color:var(--orange)}
.nav-rule{left:370px;top:86px;width:640px;height:2px;background:linear-gradient(90deg,transparent,#ddd 20%,#ddd 80%,transparent)}
.search-box{left:677px;top:100px;width:236px;height:22px;background:#fff;border:1px solid #ddd;border-radius:3px}
.search-link{left:921px;top:102px;font-family:'Jura',sans-serif;font-weight:600;font-size:13px;color:var(--orange)}
.hero-art{left:95px;top:148px;width:540px;height:285px;border-radius:6px;background:linear-gradient(135deg,#222 0,#2f78c4 40%,#d8d8d8 75%,#ececec 100%)}
.hero-title{left:636px;top:180px;white-space:nowrap;font-family:'Audiowide',sans-serif;font-weight:400;font-size:26px;color:var(--orange)}
.hero-sub{left:636px;top:218px;width:360px;font-family:'Jura',sans-serif;font-weight:500;font-size:28px;line-height:32px;color:#555}
.hero-actions{left:645px;top:328px;display:flex;align-items:center;gap:14px;font-family:'Jura',sans-serif;font-weight:600;font-size:16px;color:#666}
.hero-actions .or{color:var(--orange);font-size:13px}
.btn-dark{display:inline-block;width:190px;height:42px;line-height:42px;text-align:center;background:linear-gradient(#5a5a5a,#3e3e3e);color:#fff;border-radius:2px;box-shadow:0 2px 3px rgba(0,0,0,.3);font-size:15px}
.slider-dots{left:910px;top:440px;display:flex;gap:8px}
.slider-dots span{width:16px;height:16px;border-radius:50%;background:#e4e4e4}
.slider-dots .on{background:var(--orange)}
.hero-rule{left:60px;top:480px;width:964px;height:2px;background:linear-gradient(90deg,transparent,#ddd 20%,#ddd 80%,transparent)}
.section-title{font-family:'Jura',sans-serif;font-weight:600;font-size:20px;color:#555}
.trusted{left:95px;top:524px}
.clients{left:95px;top:572px;width:540px;display:flex;justify-content:space-between;align-items:center;font-family:'Lato',sans-serif;font-size:26px;color:#6b6b6b}
.client{display:flex;align-items:center;gap:8px}
.client i{width:20px;height:20px;border-radius:50%;background:#aab}
.divider{left:95px;top:635px;width:540px;height:1px;background:var(--line)}
.saying{left:98px;top:664px}
.quote-brand{left:100px;top:708px;display:flex;align-items:center;gap:6px;font-size:24px;color:#4a4a4a}
.quote-brand i{width:22px;height:22px;border-radius:50%;background:#555}
.quote{left:221px;top:700px;width:420px;font-size:14px;line-height:20px;color:#555}
.quote cite{display:block;margin-top:8px;font-size:12px;font-weight:700;font-style:italic;color:#555}
.more{left:541px;top:790px;font-family:'Jura',sans-serif;font-weight:600;font-size:13px;color:var(--orange)}
.contact{left:688px;top:524px}
.contact-intro{left:688px;top:553px;width:300px;font-size:13.5px;line-height:17px;color:#444}
.form{left:688px;top:600px;width:300px}
.form .row{display:flex;justify-content:space-between;align-items:center;height:34px}
.form label{font-family:'Jura',sans-serif;font-weight:600;font-size:12px;color:#444}
.form .field{width:180px;height:22px;background:#fff;border:1px solid #ddd;border-radius:2px}
.btn-orange{background:linear-gradient(#f9a149,var(--orange-dark));color:#fff;text-align:center;box-shadow:0 2px 3px rgba(0,0,0,.25);font-family:'Audiowide',sans-serif}
.contact-btn{left:856px;top:768px;width:130px;height:32px;line-height:32px;font-size:13px;border-radius:2px}
.newsletter{left:95px;top:854px;width:892px;height:96px;background:#fff;border-radius:6px 6px 0 0}
.nl-title{left:118px;top:878px;font-family:'Audiowide',sans-serif;font-weight:400;font-size:21px;color:var(--orange)}
.nl-input{top:877px;height:30px;border:1px solid #ddd;border-radius:15px;background:#fff;padding-left:20px;line-height:28px;font-family:'Jura',sans-serif;font-size:15px;color:#aaa}
.nl-name{left:339px;width:243px}
.nl-email{left:594px;width:251px}
.nl-btn{left:856px;top:876px;width:111px;height:30px;line-height:30px;border-radius:15px;font-size:14px}
.nl-text{left:118px;top:920px;font-size:13.5px;color:#444}
.band{left:0;top:948px;width:1084px;height:3px;background:#d5d5d5}
.footer{left:95px;top:996px;width:892px;height:158px;background:var(--panel);border-radius:22px;box-shadow:0 3px 0 #fff}
.f-company{left:122px;top:1016px;font-size:12.5px;font-weight:700;color:#222}
.f-address{left:122px;top:1040px;font-size:11.5px;line-height:16px;color:#444}
.f-address a{color:var(--orange);text-decoration:underline}
.f-mark{left:125px;top:1112px;width:26px;height:26px;border-radius:50%;border:3px solid #cfcfcf}
.f-copy{left:180px;top:1106px;font-size:12.5px;line-height:16px;color:#555}
.f-col{top:1016px;font-size:11px;line-height:13.5px;color:#444}
.f-col h4{font-size:12px;font-weight:700;color:#333;margin-bottom:14px}
.f-social li{display:flex;align-items:center;gap:8px;margin-bottom:4px;list-style:none}
.f-social i{width:14px;height:14px;background:#7a7a7a;border-radius:2px}
.f-col ul{list-style:none}
</style>
</head>
<body>
<div class="canvas">
  <div class="abs topbar"></div>
  <div class="abs brand"><span>KESTREL</span><span class="dot"></span><span>NINE</span></div>
  <nav class="abs nav">
    <span class="current">Who We Are?</span><span>Our Services</span><span>Testimonials</span><span>News</span><span>Contact Us</span>
  </nav>
  <div class="abs nav-rule"></div>
  <div class="abs search-box"></div>
  <div class="abs search-link">search &gt;</div>

  <div class="abs hero-art" role="img" aria-label="Group of computer devices: desktop tower, monitor, tablet, phone and laptop"></div>
  <h1 class="abs hero-title">Hello, we're Kestrel Nine.</h1>
  <p class="abs hero-sub">We provide technology services to small and medium businesses</p>
  <div class="abs hero-actions"><span>Learn more</span><span class="or">or</span><span class="btn-dark">view our services</span></div>
  <div class="abs slider-dots"><span class="on"></span><span></span><span></span></div>
  <div class="abs hero-rule"></div>

  <h2 class="abs section-title trusted">Trusted by</h2>
  <div class="abs clients">
    <span class="client">Talvio</span>
    <span class="client"><i></i>Brenholt</span>
    <span class="client">Quillmark</span>
  </div>
  <div class="abs divider"></div>
  <h2 class="abs section-title saying">What our Clients are saying!</h2>
  <div class="abs quote-brand"><i></i>Pendrel</div>
  <blockquote class="abs quote">Lorem ipsum dolor sit amet, consectetuer adipiscing elit, sed diam nonummy nibh euismod tincidunt ut laoreet dolore magna aliquam erat volutpat. Ut wisi enim ad minim veniam sed diam nonummy.<cite>—Dalton R. Ashvale, P.E. Pendrel</cite></blockquote>
  <div class="abs more">read more &gt;</div>

  <h2 class="abs section-title contact">Contact Us</h2>
  <p class="abs contact-intro">Contact us by filling out the form below or calling us at 615-382-7140</p>
  <div class="abs form">
    <div class="row"><label>FIRST NAME</label><span class="field"></span></div>
    <div class="row"><label>LAST NAME</label><span class="field"></span></div>
    <div class="row"><label>COMPANY EMAIL</label><span class="field"></span></div>
    <div class="row"><label>COMPANY NAME</label><span class="field"></span></div>
    <div class="row"><label>PHONE</label><span class="field"></span></div>
  </div>
  <div class="abs btn-orange contact-btn">CONTACT US</div>

  <div class="abs newsletter"></div>
  <h2 class="abs nl-title">Email Newsletter</h2>
  <div class="abs nl-input nl-name">Enter Name</div>
  <div class="abs nl-input nl-email">Enter Email Address</div>
  <div class="abs btn-orange nl-btn">submit</div>
  <p class="abs nl-text">Enter your email address to receive monthly updates about our latest news, events and free technology resources for your small business!</p>
  <div class="abs band"></div>

  <footer class="abs footer"></footer>
  <div class="abs f-company">Kestrel Nine LLC.</div>
  <div class="abs f-address">517 Hollis Row E Suite 812B Nashville, TN 37219<br>Phone: 615-382-7140 &nbsp;|&nbsp; <a>info@knllc.com</a> &nbsp;|&nbsp; <a>sales@knllc.com</a></div>
  <div class="abs f-mark"></div>
  <div class="abs f-copy">© Copyright 2012 Kestrel Nine LLC.<br>All Rights Reserved.</div>
  <div class="abs f-col" style="left:563px"><h4>Home</h4><ul><li>Contact Us</li><li>Sitemap</li></ul></div>
  <div class="abs f-col" style="left:646px"><h4>About Us</h4><ul><li>Overview</li><li>Executive Team</li><li>News</li><li>Events</li><li>Blog</li></ul></div>
  <div class="abs f-col" style="left:749px"><h4>Technology</h4><ul><li>Overview</li><li>Onsite Expertise</li><li>IT Design Services</li><li>Virus &amp; Spam Protection</li><li>Archiving</li></ul></div>
  <div class="abs f-col f-social" style="left:893px"><h4>Follow Us</h4><ul><li><i></i>Circlepage</li><li><i></i>Chirpline</li><li><i></i>Workroll</li><li><i></i>Reelcast</li><li><i></i>Rss Feed</li></ul></div>
</div>
</body>
</html>
```